Willowmere Physio Visits

I am a Physical Therapist. I want to go to peoples homes and give them quality one on one care for their back/thoracic/neck pain. I will give them spinal mobilizations, massage and exercise. I will do all of this in the comfort of their homes. I will bring my massage table with me so I can work on their back and neck. Fee for service. Accept check and credit cards. I am an orthopaedic specialist and a Spine specialist. I will come to your door so you don't have to come to me.

Target Market(s)

working class and upper class

Industry/Entity Type

Massage

Requirements
Nice to have
• Something to let the people know they will be treated special. They will get better care with me than if they were in an outpatient setting.

```html
<!DOCTYPE html>
<html lang="en">
<head>
<meta charset="utf-8">
<title>Willowmere Physio Visits</title>
<link rel="stylesheet" href="https://fonts.googleapis.com/css2?family=Cookie&family=Source+Sans+3:ital,wght@0,700;1,500&display=swap">
<style>
  :root {
    --page: #ffffff;
    --panel: #000000;
    --accent: #e6e95a;
    --ink-dark: #111111;
    --body-text: #c9c9c9;
    --frame: #8a8a8a;
    --photo-deep: #03070c;
    --photo-mid: #2f5e78;
    --photo-light: #8fc3da;
  }
  * { margin: 0; padding: 0; box-sizing: border-box; }
  html, body {
    width: 1200px;
    height: 930px;
    overflow: hidden;
    background: var(--page);
  }
  .flyer {
    position: relative;
    width: 1200px;
    height: 930px;
    background: var(--page);
  }
  .flyer__panel {
    position: absolute;
    left: 30px;
    top: 30px;
    width: 1140px;
    height: 870px;
    background: var(--panel);
    overflow: hidden;
  }
  .flyer__photo {
    position: absolute;
    left: 530px;
    top: 0;
    width: 610px;
    height: 870px;
    background:
      radial-gradient(ellipse 38% 48% at 52% 48%, var(--photo-light) 0%, var(--photo-mid) 45%, transparent 80%),
      radial-gradient(ellipse 55% 70% at 55% 55%, rgba(47,94,120,0.55) 0%, transparent 75%),
      var(--photo-deep);
  }
  .flyer__title {
    position: absolute;
    left: 46px;
    top: 68px;
    font-family: "Cookie", cursive;
    font-weight: 400;
    font-size: 96px;
    line-height: 1;
    color: var(--accent);
    white-space: nowrap;
  }
  .flyer__frame {
    position: absolute;
    left: 42px;
    top: 167px;
    width: 528px;
    height: 665px;
    border: 2px solid var(--frame);
    border-radius: 14px;
  }
  .flyer__badge {
    position: absolute;
    left: 213px;
    top: 152px;
    height: 51px;
    padding: 0 10px;
    background: var(--accent);
    font-family: "Source Sans 3", sans-serif;
    font-weight: 700;
    font-size: 42px;
    line-height: 51px;
    color: var(--ink-dark);
    white-space: nowrap;
  }
  .flyer__copy {
    position: absolute;
    left: 80px;
    top: 280px;
    width: 444px;
    font-family: "Source Sans 3", sans-serif;
    font-style: italic;
    font-weight: 500;
    font-size: 24.5px;
    line-height: 33px;
    letter-spacing: 0.3px;
    color: var(--body-text);
    text-align: justify;
    hyphens: manual;
  }
  .flyer__copy p { text-indent: 120px; }
  .flyer__copy p + p { text-indent: 36px; }
</style>
</head>
<body>
  <main class="flyer">
    <section class="flyer__panel">
      <div class="flyer__photo" role="img" aria-label="Photograph of a person's bare back in cool blue light, hands on the lower back, with a glowing multicoloured spine highlighted down the centre"></div>

      <h1 class="flyer__title">Willowmere</h1>
      <div class="flyer__frame"></div>
      <div class="flyer__badge">Physio Visits</div>

      <div class="flyer__copy">
        <p>I am a Physical Therapist. I want to go to peoples homes and give them quality one on one care for their back / thoracic / neck pain. I will give them spinal mobili&shy;zations, massage and exercise. I will do all of this in the comfort of their homes. I will bring my massage table with me so I can work on their back and neck. Fee for service. Accept check and credit cards.</p>
        <p>I am an orthopaedic specialist and a Spine specialist. I will come to your door so you don't have to come to me.</p>
      </div>
    </section>
  </main>
</body>
</html>
```